High-End Medical Center Website Design Project

This design is part of a well thought-out project by an experienced project manager / developer. The approved wireframe is attached. Creative interpretations / suggestions based on the layout encouraged.

The design is for a new state-of-the-art medical center located in Dallas, Texas. The target audience would likely be individuals (approx. 60% female /40% male) who are the healthcare decision-makers for their families. They would likely have insurance and be inclined to seek out top-quality care.

Potential clients would choose this client over others in their industry because the medical center is physician owned, meaning it is patient-focused rather than profit-focused. The facility is brand new, featuring the latest technology. (This includes an amazing waiting room featuring WiFi and docking stations.) The physicians are hand-picked by referral only.

The look of the site should be extremely clean. We are going for a well-organized, professional look with a bit of a warm glow (interpret that however you like). Use crisp corners and the colors in the logo.

Think modern, clean with some great use of color / font.

We can get lovely photography of the medical center once construction is complete. Feel free to use an "example image" behind the Featured Area ("Physician Owned. Patient-Focused") if you like. We are open to ideas.

ONE CHANGE REQUESTED IN THE WIREFRAME:

Remove the "Connect" 1/4 page footer area and replace with a quick contact form. You may swap the "Locations" area with the form if desired. Put social media icons at the top left of the page in the top header area.

(Note: Please use social media icons that match the design rather than standard icons. We preferred not placing the icons at the top, but the client requested this. Let's not bring more attention to them than necessary.)
Updates

We're custom programming this site, so there's no need to base it on a template. Also, we would prefer not to use typical "seen everywhere" stock images.Thanks.

Industry/Entity Type

Construction

Requirements
Must have
• Follow the wireframe. This has been approved.
Nice to have
• Examples of what hover states, links or dropdowns might look like.

```html
<!DOCTYPE html>
<html lang="en">
<head>
<meta charset="utf-8">
<title>Northvale Medical Center</title>
<link rel="stylesheet" href="https://fonts.googleapis.com/css2?family=Montserrat:wght@400;600;700&family=Arimo:wght@400;700&display=swap">
<style>
:root{
  --teal:#4aaeba;
  --teal-dark:#3a9ca8;
  --blue:#0d5fa9;
  --blue-deep:#0a4f93;
  --orange:#f05a28;
  --ink:#111111;
  --grey:#555555;
  --line:#dcdcdc;
  --white:#ffffff;
}
*{box-sizing:border-box;margin:0;padding:0}
html,body{width:1145px;height:1200px;overflow:hidden;background:var(--white)}
body{position:relative;font-family:"Arimo",Arial,sans-serif;color:var(--ink)}
.abs{position:absolute}

/* header */
.site-header{left:135px;top:0;width:870px;height:116px;background:var(--teal);border-bottom:3px solid var(--blue)}
.phone-tab{left:699px;top:0;width:171px;height:27px;background:var(--blue);color:var(--white);
  font:600 14px "Montserrat",sans-serif;display:flex;align-items:center;gap:6px;padding-left:44px;
  clip-path:polygon(28px 0,100% 0,100% 100%,44px 100%)}
.phone-tab svg{width:13px;height:13px}
.phone-stripes{left:699px;top:0;width:40px;height:27px}
.brand{left:20px;top:28px;height:42px;display:flex;align-items:center;gap:8px;background:var(--blue);padding:0 12px;
  color:var(--white);font:700 24px "Montserrat",sans-serif;letter-spacing:.5px}
.brand-dot{width:14px;height:14px;border-radius:50%;background:var(--white)}
.main-nav{left:25px;top:84px;display:flex;gap:33px;list-style:none}
.main-nav a{color:var(--white);text-decoration:none;font:600 14px "Montserrat",sans-serif;letter-spacing:.3px}
.nav-active{left:23px;top:110px;width:91px;height:6px;background:var(--blue)}

/* hero */
.hero-photo{left:49px;top:116px;width:1047px;height:367px;
  background:linear-gradient(90deg,rgba(255,255,255,1) 0%,rgba(228,238,243,.9) 12%,#d7e6ee 35%,#c5d9e6 60%,#b7cfe0 80%,rgba(230,240,246,.8) 95%,rgba(255,255,255,1) 100%)}
.hero-copy{left:134px;top:210px}
.hero-title{font:700 33px/1.1 "Montserrat",sans-serif;color:var(--ink);letter-spacing:-.5px}
.hero-title span{display:block;color:var(--blue);font-size:37px;letter-spacing:-1px}
.hero-sub{font-size:16px;margin-top:6px}
.service-list{left:134px;top:323px;display:flex;gap:26px}
.service{width:70px;text-align:center;font-size:12px}
.service-ring{width:70px;height:70px;border-radius:50%;border:2px solid var(--blue);background:var(--white);
  display:flex;align-items:center;justify-content:center;margin-bottom:9px}
.service-ring svg{width:34px;height:34px}
.slider-dots{left:978px;top:455px;display:flex;gap:2px}
.slider-dots i{width:8px;height:8px;border-radius:50%;background:#777}
.slider-dots i:first-child{background:var(--blue)}

/* features */
.intro-heading{left:135px;top:517px;width:140px;color:var(--blue);font:600 19px/1.3 "Montserrat",sans-serif}
.feature{top:518px;width:220px}
.feature h3{font:600 18px "Montserrat",sans-serif;margin-bottom:8px}
.feature p{font-size:11.5px;line-height:1.4}

/* content panel */
.panel{left:136px;top:634px;width:869px;height:250px;border:1px solid var(--line);border-bottom:none;box-shadow:0 0 4px rgba(0,0,0,.08)}
.panel-divider{left:708px;top:634px;width:1px;height:250px;background:var(--line)}
.building-photo{left:160px;top:672px;width:263px;height:156px;background:linear-gradient(180deg,#aecbe0 0%,#c7d8e4 45%,#8a7a62 70%,#e6e8ea 100%)}
.block-title{font:600 18px "Montserrat",sans-serif}
.whatwedo{left:442px;top:676px;width:250px}
.whatwedo p{font-size:12.5px;line-height:1.3;margin-top:12px}
.btn{display:inline-block;background:var(--orange);color:var(--white);font:400 10px "Montserrat",sans-serif;
  text-transform:uppercase;padding:4px 13px;border:1px solid #c94314;text-decoration:none}
.whatwedo .btn{margin-top:10px}
.quote-mark{left:712px;top:565px;font:700 260px/1 Georgia,serif;color:#eeeeee}
.testimonial{left:744px;top:677px;width:240px}
.testimonial p{font-size:11.5px;line-height:1.4;margin-top:12px}
.author{display:flex;align-items:center;gap:14px;margin-top:14px;font-size:12px;line-height:1.4}
.author-photo{width:37px;height:37px;background:linear-gradient(#d9c2ad,#8d9aa8)}
.close-quote{left:954px;top:796px;font:700 30px Georgia,serif;color:#999}
.testimonial .btn{margin-top:16px}

/* footer */
.site-footer{left:135px;top:883px;width:870px;height:272px;background:var(--blue)}
.footer-col{top:924px;color:var(--white)}
.footer-col h4{font:400 16px "Montserrat",sans-serif;margin-bottom:17px}
.post{font-size:11.5px;line-height:1.25;margin-bottom:12px}
.post small{display:block;font-size:10px}
.contact-form{display:flex;flex-direction:column;gap:3px}
.field{width:178px;height:27px;background:var(--white);border:1px solid #c9d7e6;color:#888;font-size:11px;padding:6px 7px}
.field.tall{height:57px;margin-top:2px}
.form-btn{margin-top:8px;width:106px;height:24px;background:var(--orange);color:var(--white);font:400 11px "Montserrat",sans-serif;
  display:flex;align-items:center;justify-content:center;border:1px solid #ff8a62}
.wait{display:flex;gap:13px}
.wait-badge{flex:none;width:52px;height:52px;border-radius:50%;background:var(--white);color:var(--blue);
  font:400 19px "Montserrat",sans-serif;display:flex;align-items:center;justify-content:center;margin-top:-2px}
.wait p{font-size:12px;line-height:1.47;width:82px;margin-top:-7px}

.legal-bar{left:135px;top:1155px;width:870px;height:45px;background:var(--teal);color:var(--white);font-size:10.5px;
  display:flex;align-items:center;padding-left:24px;gap:12px}
.social{position:absolute;right:20px;top:11px;display:flex;gap:8px}
.social i{width:24px;height:24px;border-radius:50%;border:1px solid var(--white)}
</style>
</head>
<body>

<header class="abs site-header">
  <svg class="abs phone-stripes" viewBox="0 0 40 27"><path d="M0 0h8l16 27h-8z M12 0h8l16 27h-8z" fill="#fff"/></svg>
  <div class="abs phone-tab">
    <svg viewBox="0 0 16 16"><path d="M3 1l3 3-1.5 2a9 9 0 0 0 5.5 5.5L12 10l3 3-2 2C7 15 1 9 1 3z" fill="#fff"/></svg>
    (555) 214 0186
  </div>
  <div class="abs brand"><span class="brand-dot"></span>NORTHVALE MEDICAL CENTER</div>
  <ul class="abs main-nav">
    <li><a href="#">WHY NORTHVALE</a></li>
    <li><a href="#">PHYCISIANS</a></li>
    <li><a href="#">SPECIALITIES</a></li>
    <li><a href="#">INFO</a></li>
    <li><a href="#">LOCATIONS</a></li>
    <li><a href="#">CONTACT</a></li>
  </ul>
  <div class="abs nav-active"></div>
</header>

<section>
  <div class="abs hero-photo" role="img" aria-label="Team of smiling doctors and nurses in white coats and scrubs"></div>
  <div class="abs hero-copy">
    <h1 class="hero-title">Physician Owned<span>Patient Focused</span></h1>
    <p class="hero-sub">Lorem ipsum dolor sit consectetur</p>
  </div>
  <div class="abs service-list">
    <div class="service"><div class="service-ring">
      <svg viewBox="0 0 34 34" fill="none" stroke="#2f7fbf" stroke-width="2.5" stroke-linecap="round"><path d="M10 4v8a6 6 0 0 0 12 0V4M16 18v5a5 5 0 0 0 10 0v-3"/><circle cx="26" cy="17" r="3"/></svg>
    </div>tempor</div>
    <div class="service"><div class="service-ring">
      <svg viewBox="0 0 34 34"><rect x="4" y="10" width="26" height="18" rx="2" fill="#2f7fbf"/><path d="M12 10V6h10v4" fill="none" stroke="#2f7fbf" stroke-width="2.5"/><circle cx="17" cy="19" r="6" fill="#fff"/><path d="M17 15.5v7M13.5 19h7" stroke="#2f7fbf" stroke-width="2"/></svg>
    </div>tempor</div>
    <div class="service"><div class="service-ring">
      <svg viewBox="0 0 34 34" fill="none" stroke="#2f7fbf" stroke-width="2.5" stroke-linecap="round"><path d="M3 10l5 10h20l4-6M8 20l-3 6M28 20l3 6"/><circle cx="11" cy="28" r="2"/><circle cx="25" cy="28" r="2"/><path d="M10 15l5 3 10-6" /></svg>
    </div>tempor</div>
  </div>
  <div class="abs slider-dots"><i></i><i></i><i></i></div>
</section>

<section>
  <h2 class="abs intro-heading">lorem ipsum dolor sit amet consecte</h2>
  <article class="abs feature" style="left:300px"><h3>Technology</h3><p>Lorem ipsum dolor sit amet, elit tempor incididunt ut labore et dolore magna aliqua ut enim ad minim...</p></article>
  <article class="abs feature" style="left:552px"><h3>Quality of Care</h3><p>Lorem ipsum dolor sit amet, elit tempor incididunt ut labore et dolore magna aliqua ut enim ad minim...</p></article>
  <article class="abs feature" style="left:798px"><h3>Patient Experience</h3><p>Lorem ipsum dolor sit amet, elit tempor incididunt ut labore et dolore magna aliqua ut enim ad minim...</p></article>
</section>

<section>
  <div class="abs panel"></div>
  <div class="abs panel-divider"></div>
  <div class="abs building-photo" role="img" aria-label="Modern medical center building with a curved glass facade"></div>
  <div class="abs whatwedo">
    <h3 class="block-title">What we do ?</h3>
    <p>Lorem ipsum dolor sit amet, consectetur adipisicing elit, sed do eiusmod tempor incididunt ut labore et dolore magna aliqua. Ut enim ad minim veniam, quis nostrud exercitation ullamco laboris nisi ut aliquip ex ea commodo consequat.</p>
    <a class="btn" href="#">Learn More</a>
  </div>
  <div class="abs quote-mark" aria-hidden="true">&ldquo;</div>
  <div class="abs testimonial">
    <h3 class="block-title">Testimonials</h3>
    <p>Lorem ipsum dolor sit amet, consectetur adipisicing elit, sed do eiusmod tempor incididunt ut labore et dolore magna aliqua. Ut enim ad minim veniam,</p>
    <div class="author">
      <div class="author-photo" role="img" aria-label="Portrait of the reviewing surgeon"></div>
      <div>Dr. Alan Mercer<br>Sr. Surgen - USA</div>
    </div>
    <a class="btn" href="#">Learn More</a>
  </div>
  <div class="abs close-quote" aria-hidden="true">&rdquo;</div>
</section>

<footer>
  <div class="abs site-footer"></div>
  <div class="abs footer-col" style="left:166px">
    <h4>News</h4>
    <div class="post">Lorem ipsum dolor sit amet sed..<small>22 July, 2013 &nbsp; | &nbsp;Read More</small></div>
    <div class="post">Lorem ipsum dolor sit amet sed..<small>22 July, 2013 &nbsp; | &nbsp;Read More</small></div>
    <div class="post">Lorem ipsum dolor sit amet sed..<small>22 July, 2013 &nbsp; | &nbsp;Read More</small></div>
  </div>
  <div class="abs footer-col" style="left:377px">
    <h4>Blog</h4>
    <div class="post" style="margin-bottom:18px">Consectetur adipisicing<br>Lorem ipsum dolor sit amet sed<small>22 July, 2013 &nbsp; | &nbsp;Read More</small></div>
    <div class="post">Consectetur adipisicing<br>Lorem ipsum dolor sit amet sed<small>22 July, 2013 &nbsp; | &nbsp;Read More</small></div>
  </div>
  <div class="abs footer-col" style="left:596px">
    <h4>Quick Contact</h4>
    <form class="contact-form" style="margin-left:3px">
      <div class="field">Name</div>
      <div class="field">Email</div>
      <div class="field tall">Comment</div>
      <div class="form-btn">CONTACT US</div>
    </form>
  </div>
  <div class="abs footer-col" style="left:825px">
    <h4>Average Wait Time</h4>
    <div class="wait"><div class="wait-badge">01</div><p>Consectetur adipisicing Lorem ipsum dolor sit amet sed adipisicing elit, sed do</p></div>
  </div>
  <div class="abs legal-bar">
    <span>All Right Reserved &copy; Copyright with www.northvale-mc.com &nbsp;- &nbsp;2013</span>
    <span>Terms &nbsp;. &nbsp;Privacy Policy</span>
    <div class="social"><i></i><i></i><i></i><i></i><i></i></div>
  </div>
</footer>

</body>
</html>
```